Custom Proposal

We need a custom proposal template created for our company. Our company, BRIGHTWAVE AUDIO SERVICES, provides in-store music and messaging services to businesses in the US and Canada. We need a 3-4 page document created that outlines our products and services that will accompany their proposal. The proposal needs to be created using company colors with a fresh feeling. Our music service is top quality and we service many major brands with customized music service. We have all of the copy and logos for partner companies. We need a designer to create a layout that will express our products and services in a fresh and exciting way.

Attached to this project you will find the following:

- PDF file title "Example". This is an example file of what we are looking for (minus the last page with the order fields).

- BRIGHTWAVE AUDIO SERVICES logo in EPS

- BRIGHTWAVE AUDIO SERVICES brand standards guideline

- Text copy for the flyer

- Styles (these match our web site)

- Font used on our web site and other material

- Zip file with logos of companies we do business with

We would also like a section that has the logos for these companies to showcase who we work with.

We prefer to have the project developed in an editable format such as Adobe Illustrator or PSD.

The paper size is 8 1/2" x 11" Portrait
Updates

Please note: We do NOT want the graphics included in the "Brands Standard Guide" that is attached to the project to be used for the project. The Brand Standards Guide is provided simply to show you how to use our logo, not to include the graphics used in the guide. Also, we do not want any computers or smart phones in the artwork. We provided the Pelican Harbor document as an example of one we liked, not to use the same graphics.

Please be sure to follow the outline of the project and use the images  supplied. Please also keep in mind we  are not looking for a template look  but rather  a  unique design  for each page that is themed for our industry. Our industry is in-store music and messaging services.

Thank you

Target Market(s)

Business owners, executives, marketing directors, business executives

Industry/Entity Type

Business

Requirements
Must have
• We are looking for fresh, open, personal, exciting, creative, and relevant designs.
Should not have
• We are NOT looking for stock template looking designs with no originality that look like a standard stock design.

```html
<!DOCTYPE html>
<html lang="en">
<head>
<meta charset="utf-8">
<title>Brightwave Audio Services – About &amp; Services</title>
<link rel="stylesheet" href="https://fonts.googleapis.com/css2?family=Open+Sans:wght@300;400;600;700;800&display=swap">
<style>
  :root{
    --green:#a2c41f;
    --green-dark:#7f9e12;
    --heading-green:#8cb219;
    --bar-grey:#4a4a4c;
    --text:#5b5b5b;
    --page:#ffffff;
    --page-shade:#e9e9ea;
    --band-dark:#05070d;
    --band-blue:#2a6fc4;
  }
  *{margin:0;padding:0;box-sizing:border-box;}
  html,body{width:1200px;height:833px;overflow:hidden;background:#fff;}
  body{position:relative;font-family:"Open Sans",Arial,sans-serif;color:var(--text);}

  .page{position:absolute;top:52px;height:766px;
    background:linear-gradient(to bottom,var(--page) 0%,var(--page) 62%,var(--page-shade) 100%);}
  .page--left{left:15px;width:575px;}
  .page--right{left:613px;width:565px;}

  .masthead{position:absolute;left:0;top:0;width:100%;height:78px;}
  .masthead svg{position:absolute;inset:0;width:100%;height:100%;}
  .masthead__title{position:absolute;left:26px;top:14px;font-size:38px;font-weight:700;color:#fff;letter-spacing:.5px;line-height:50px;}

  .section-bar{position:absolute;left:0;height:29px;}
  .section-bar svg{position:absolute;inset:0;width:100%;height:100%;}
  .section-bar__label{position:absolute;left:26px;top:3px;font-size:17.5px;font-weight:700;color:#fff;line-height:23px;letter-spacing:.2px;}
  .page--right .section-bar__label{left:19px;}

  .heading{position:absolute;font-size:10.6px;font-weight:700;color:var(--heading-green);text-transform:uppercase;line-height:11.5px;letter-spacing:.1px;}
  .copy{position:absolute;font-size:9.2px;font-weight:400;line-height:11.4px;text-align:justify;color:var(--text);}
  .copy p+p{margin-top:9px;}
  .copy ul{list-style:none;}
  .copy li::before{content:"\2022";color:var(--heading-green);margin-right:4px;}

  .photo{position:absolute;height:146px;}
  .photo svg{width:100%;height:100%;display:block;}

  .partners{position:absolute;left:26px;top:685px;display:flex;align-items:center;gap:16px;}
  .partner{display:flex;align-items:center;gap:4px;font-size:12px;font-weight:700;color:#3f3f3f;}
  .partner__mark{width:9px;height:9px;background:var(--bar-grey);}
</style>
</head>
<body>

<!-- LEFT PAGE -->
<section class="page page--left">
  <header class="masthead">
    <svg viewBox="0 0 575 78" preserveAspectRatio="none">
      <defs>
        <linearGradient id="waveL" x1="0" y1="0" x2="0" y2="1">
          <stop offset="0" stop-color="#05070d"/>
          <stop offset=".5" stop-color="#1f5fb8"/>
          <stop offset="1" stop-color="#05070d"/>
        </linearGradient>
      </defs>
      <rect x="0" y="0" width="575" height="78" fill="var(--band-dark)"/>
      <rect x="250" y="22" width="325" height="34" fill="url(#waveL)" opacity=".85" role="img" aria-label="Glowing blue sound wave graphic"/>
      <polygon points="0,0 280,0 240,78 0,78" fill="var(--green)"/>
      <polygon points="272,0 280,0 240,78 232,78" fill="var(--green-dark)"/>
    </svg>
    <h1 class="masthead__title">ABOUT</h1>
  </header>

  <h2 class="heading" style="left:26px;top:93px;">Experience the Brightwave advantage.</h2>
  <div class="copy" style="left:26px;top:105px;width:318px;">
    <p>BRIGHTWAVE AUDIO SERVICES™ is committed to delivering businesses the marketing advantage of providing licensed, in-store music and messaging, customized for their consumers. Using real-time management of media players at national, regional and local store levels, BRIGHTWAVE AUDIO SERVICES™ aims to carry out a strategically developed mission, backed by a vision designed to specifically meet client needs and the needs of their consumers.</p>
  </div>

  <h2 class="heading" style="left:26px;top:197px;">Our Mission</h2>
  <div class="copy" style="left:26px;top:209px;width:318px;">
    <p>To provide quality in-store music and messaging services empowered by hard work, ingenuity, and integrity.</p>
    <p>To realize this mission, we have developed an industry leading solution for the delivery and management of digital assets that combines the power of the Internet with the flexibility of software.</p>
  </div>

  <h2 class="heading" style="left:26px;top:284px;">Our Vision</h2>
  <div class="copy" style="left:26px;top:296px;width:318px;">
    <p>Producing innovative and affordable business audio solutions, utilizing the latest technology and the brightest minds.</p>
  </div>

  <figure class="photo" style="left:357px;top:97px;width:206px;">
    <svg viewBox="0 0 206 146" preserveAspectRatio="none">
      <defs><linearGradient id="p1" x1="0" y1="0" x2="1" y2="1"><stop offset="0" stop-color="#d9d9d6"/><stop offset="1" stop-color="#8c8c8a"/></linearGradient></defs>
      <rect x="14" y="0" width="192" height="146" fill="url(#p1)" role="img" aria-label="Photo of a cheerful office worker on the phone"/>
      <polygon points="0,0 22,0 16,146 6,146" fill="var(--green)"/>
    </svg>
  </figure>

  <div class="section-bar" style="top:347px;width:208px;">
    <svg viewBox="0 0 208 29" preserveAspectRatio="none"><polygon points="0,0 208,0 192,29 0,29" fill="var(--bar-grey)"/></svg>
    <span class="section-bar__label">WHY BRIGHTWAVE?</span>
  </div>

  <h2 class="heading" style="left:26px;top:388px;">Take your business to the next level.</h2>
  <div class="copy" style="left:26px;top:401px;width:318px;">
    <p>As the leading provider of audio, video and messaging services for businesses throughout the US, we offer quality products and services coupled with premium customer support to deliver a unique and stress-free streaming music solution for our customers.</p>
    <p style="text-align:left;margin-top:11px;">Experience the optimal advantage with BRIGHTWAVE AUDIO SERVICES™</p>
  </div>

  <figure class="photo" style="left:355px;top:346px;width:208px;">
    <svg viewBox="0 0 208 146" preserveAspectRatio="none">
      <defs><linearGradient id="p2" x1="0" y1="0" x2="0" y2="1"><stop offset="0" stop-color="#c9c3b6"/><stop offset="1" stop-color="#8a8174"/></linearGradient></defs>
      <rect x="14" y="0" width="194" height="146" fill="url(#p2)" role="img" aria-label="Photo of a bright shopping mall interior"/>
      <polygon points="0,0 22,0 16,146 6,146" fill="var(--green)"/>
    </svg>
  </figure>

  <div class="section-bar" style="top:522px;width:208px;">
    <svg viewBox="0 0 208 29" preserveAspectRatio="none"><polygon points="0,0 208,0 192,29 0,29" fill="var(--bar-grey)"/></svg>
    <span class="section-bar__label">TECHNOLOGY</span>
  </div>

  <h2 class="heading" style="left:26px;top:561px;">Get tomorrow’s technology, today.</h2>
  <div class="copy" style="left:26px;top:573px;width:318px;">
    <p>BRIGHTWAVE AUDIO SERVICES™ employs our own propriety software solutions, both built and hosted on a best-in-class, Class-A hybrid foundation. Our application and database servers live within the Stackhaven Enterprise Cloud Network, whereas our Digital Asset Delivery is hosted within the Corvana Intelligent Platform with all data synced in real-time via the Corvana API. By utilizing the Stackhaven Cloud Network and the Corvana Intelligent Platform we are able to ramp up distribution and support for an unlimited number of media devices on a global scale.</p>
  </div>

  <figure class="photo" style="left:357px;top:539px;width:206px;">
    <svg viewBox="0 0 206 146" preserveAspectRatio="none">
      <defs><linearGradient id="p3" x1="0" y1="0" x2="1" y2="1"><stop offset="0" stop-color="#9a9ea4"/><stop offset="1" stop-color="#2e3136"/></linearGradient></defs>
      <rect x="14" y="0" width="192" height="146" fill="url(#p3)" role="img" aria-label="Photo of a hand on an audio mixing console"/>
      <polygon points="0,0 22,0 16,146 6,146" fill="var(--green)"/>
    </svg>
  </figure>

  <div class="partners">
    <span class="partner">Corvana</span>
    <span class="partner">Stackhaven</span>
    <span class="partner"><span class="partner__mark"></span>Northgate</span>
    <span class="partner">Flowcast</span>
  </div>
</section>

<!-- RIGHT PAGE -->
<section class="page page--right">
  <header class="masthead">
    <svg viewBox="0 0 565 78" preserveAspectRatio="none">
      <defs>
        <linearGradient id="waveR" x1="0" y1="0" x2="0" y2="1">
          <stop offset="0" stop-color="#05070d"/>
          <stop offset=".5" stop-color="#1f5fb8"/>
          <stop offset="1" stop-color="#05070d"/>
        </linearGradient>
      </defs>
      <rect x="0" y="0" width="565" height="78" fill="var(--band-dark)"/>
      <rect x="250" y="22" width="315" height="34" fill="url(#waveR)" opacity=".85" role="img" aria-label="Glowing blue sound wave graphic"/>
      <polygon points="0,0 280,0 240,78 0,78" fill="var(--green)"/>
      <polygon points="272,0 280,0 240,78 232,78" fill="var(--green-dark)"/>
    </svg>
    <h1 class="masthead__title" style="left:25px;">SERVICES</h1>
  </header>

  <h2 class="heading" style="left:20px;top:110px;">Full service in-store music solutions.</h2>
  <div class="copy" style="left:20px;top:122px;width:319px;">
    <p>INSTALLATION BRIGHTWAVE AUDIO SERVICES™ offers a wide array of services to meet a variety of needs for a range of business sizes and budgets. Our goal is simple, pinpoint and deploy optimal messaging for your brand and boost your business by creating a truly unique experience for you</p>
  </div>

  <h2 class="heading" style="left:20px;top:188px;">We do everything.</h2>
  <div class="copy" style="left:20px;top:200px;width:319px;">
    <p>Trust our professionals to handle your installation and servicing. With over 8,000 trained, licensed and insured technicians and installers at your disposal, nationwide, we’ve covered every zip code in the country. We’ll even train your staff on the proper use of your new equipment when we complete your installation.</p>
  </div>

  <figure class="photo" style="left:359px;top:107px;width:206px;">
    <svg viewBox="0 0 206 146" preserveAspectRatio="none">
      <defs><linearGradient id="p4" x1="0" y1="0" x2="1" y2="1"><stop offset="0" stop-color="#c97a3a"/><stop offset="1" stop-color="#5b3a22"/></linearGradient></defs>
      <rect x="14" y="0" width="192" height="146" fill="url(#p4)" role="img" aria-label="Photo of smiling staff at a shop counter"/>
      <polygon points="0,0 22,0 16,146 6,146" fill="var(--green)"/>
    </svg>
  </figure>

  <div class="section-bar" style="top:286px;width:292px;">
    <svg viewBox="0 0 292 29" preserveAspectRatio="none"><polygon points="0,0 292,0 276,29 0,29" fill="var(--bar-grey)"/></svg>
    <span class="section-bar__label">SERVICE LEVEL AGREEMENT</span>
  </div>

  <h2 class="heading" style="left:20px;top:330px;">SLA’S</h2>
  <div class="copy" style="left:20px;top:341px;width:319px;">
    <p>Warranty your investment and ensure the least amount of downtime with our Service Level Agreements, complete with customized warranty and service solutions, tailored to meet your needs.</p>
    <ul style="text-align:left;">
      <li>Damaged or Defective Equipment Replacement</li>
      <li>On-site Service Assistance by a Trained Technician</li>
    </ul>
  </div>

  <figure class="photo" style="left:358px;top:281px;width:207px;">
    <svg viewBox="0 0 207 146" preserveAspectRatio="none">
      <defs><linearGradient id="p5" x1="0" y1="0" x2="1" y2="1"><stop offset="0" stop-color="#e5e3df"/><stop offset="1" stop-color="#6c6a66"/></linearGradient></defs>
      <rect x="14" y="0" width="193" height="146" fill="url(#p5)" role="img" aria-label="Photo of business people reviewing a document together"/>
      <polygon points="0,0 22,0 16,146 6,146" fill="var(--green)"/>
    </svg>
  </figure>

  <div class="section-bar" style="top:444px;width:292px;">
    <svg viewBox="0 0 292 29" preserveAspectRatio="none"><polygon points="0,0 292,0 276,29 0,29" fill="var(--bar-grey)"/></svg>
    <span class="section-bar__label">CUSTOM SOLUTIONS</span>
  </div>

  <h2 class="heading" style="left:20px;top:480px;">We all have different needs.</h2>
  <div class="copy" style="left:20px;top:494px;width:319px;">
    <p>BRIGHTWAVE AUDIO SERVICES™ provides our customers and yours with streaming music services and fully customized streaming radio on a network developed specifically for your business. Each hour consists of a great mix of music and optimal messaging, selected and tailored to amplify your brand in the best way possible. All music is streamed via Internet connection utilizing a digital media player that we install for you.</p>
  </div>

  <figure class="photo" style="left:358px;top:445px;width:207px;">
    <svg viewBox="0 0 207 146" preserveAspectRatio="none">
      <defs><linearGradient id="p6" x1="0" y1="0" x2="1" y2="1"><stop offset="0" stop-color="#f4ece6"/><stop offset="1" stop-color="#d23c4a"/></linearGradient></defs>
      <rect x="14" y="0" width="193" height="146" fill="url(#p6)" role="img" aria-label="Photo of a woman enjoying music on headphones"/>
      <polygon points="0,0 22,0 16,146 6,146" fill="var(--green)"/>
    </svg>
  </figure>

  <div class="section-bar" style="top:606px;width:292px;">
    <svg viewBox="0 0 292 29" preserveAspectRatio="none"><polygon points="0,0 292,0 276,29 0,29" fill="var(--bar-grey)"/></svg>
    <span class="section-bar__label">FRANCHISE SOLUTIONS</span>
  </div>

  <h2 class="heading" style="left:20px;top:642px;width:300px;">Affordable, standardized &amp; hassle-free to meet your needs.</h2>
  <div class="copy" style="left:20px;top:668px;width:319px;">
    <p>We know that franchises and chain stores are looking for the most straightforward solution in a digital media and messaging service. That’s why we offer easy-to-use, accessible, quality audio and messaging services. Cover one, a few or all franchise locations with confidence and enjoy exclusive benefits.</p>
  </div>

  <figure class="photo" style="left:358px;top:612px;width:207px;height:145px;">
    <svg viewBox="0 0 207 145" preserveAspectRatio="none">
      <defs><linearGradient id="p7" x1="0" y1="0" x2="1" y2="1"><stop offset="0" stop-color="#b88a5a"/><stop offset="1" stop-color="#3a2418"/></linearGradient></defs>
      <rect x="14" y="0" width="193" height="145" fill="url(#p7)" role="img" aria-label="Photo of friends sharing a meal at a restaurant"/>
      <polygon points="0,0 22,0 16,145 6,145" fill="var(--green)"/>
    </svg>
  </figure>
</section>

</body>
</html>
```